I need this done FAST!
Business Cards and Stationary for new home construction company - Construction
Simple
Gerald Finch
Owner
4816 Marlow Ct #306142 Houston, TX 77391
Gerald@thequillstoneframeworks.com
www.thequillstoneframeworks.com
I would like this business card to be minimal in its design. I just want it to be a way of saying ... Hi, call me directly. It does not need to be an advertisement. I need the vector files of this please
Front should be the logo only, and the back should be this information: Design~Build Firm Gerald Finch, Owner Phone Email Web address

```html
<!DOCTYPE html>
<html lang="en">
<head>
<meta charset="utf-8">
<title>Quillstone Frameworks – Business Cards</title>
<link href="https://fonts.googleapis.com/css2?family=Montserrat:wght@400;500;700&display=swap" rel="stylesheet">
<style>
  :root {
    --bg: #e9e9e9;
    --card: #ffffff;
    --brand-red: #c1272d;
    --text-grey: #6b6b6b;
    --text-dark: #4a4a4a;
    --rule: #d8d8d8;
  }
  * { box-sizing: border-box; margin: 0; padding: 0; }
  html, body {
    width: 1200px; height: 906px; overflow: hidden;
    background: var(--bg);
    font-family: "Montserrat", Arial, sans-serif;
  }
  .sheet {
    width: 1200px; height: 906px;
    display: flex; align-items: center; justify-content: center; gap: 40px;
  }
  .card {
    width: 540px; height: 309px;
    background: var(--card);
    box-shadow: 0 6px 18px rgba(0,0,0,0.12);
    position: relative;
  }
  .brand {
    display: flex; align-items: center; gap: 10px;
    color: var(--brand-red);
    font-weight: 700; text-transform: uppercase; letter-spacing: 1px;
  }
  .brand-square { background: var(--brand-red); flex: none; }

  /* Front */
  .card-front { display: flex; align-items: center; justify-content: center; }
  .card-front .brand { font-size: 26px; }
  .card-front .brand-square { width: 22px; height: 22px; }

  /* Back */
  .card-back .brand {
    position: absolute; top: 62px; left: 0; right: 0; justify-content: center;
    font-size: 18px;
  }
  .card-back .brand-square { width: 15px; height: 15px; }
  .person {
    position: absolute; top: 104px; left: 0; right: 0; text-align: center;
  }
  .person-name {
    font-size: 13px; font-weight: 500; color: var(--text-dark);
    letter-spacing: 2px; text-transform: uppercase;
  }
  .person-title {
    font-size: 8px; color: var(--text-grey); letter-spacing: 1.5px;
    text-transform: uppercase; margin-top: 4px;
  }
  .firm-type {
    font-size: 7px; color: var(--text-grey); letter-spacing: 1px; margin-top: 3px;
  }
  .contact-list {
    position: absolute; bottom: 34px; list-style: none;
    display: flex; flex-direction: column; gap: 9px;
  }
  .contact-list.left { left: 28px; }
  .contact-list.right { left: 290px; }
  .contact-item {
    display: flex; align-items: center; gap: 8px;
    font-size: 8px; color: var(--text-grey); line-height: 1.3;
  }
  .contact-icon {
    width: 14px; height: 14px; flex: none;
    background: var(--brand-red);
    display: flex; align-items: center; justify-content: center;
  }
  .contact-icon svg { width: 9px; height: 9px; }
</style>
</head>
<body>
<main class="sheet">

  <section class="card card-front" aria-label="Business card front">
    <div class="brand"><span class="brand-square"></span>Quillstone Frameworks</div>
  </section>

  <section class="card card-back" aria-label="Business card back">
    <div class="brand"><span class="brand-square"></span>Quillstone Frameworks</div>

    <div class="person">
      <p class="person-name">Gerald Finch</p>
      <p class="person-title">Owner</p>
      <p class="firm-type">Design~Build Firm</p>
    </div>

    <ul class="contact-list left">
      <li class="contact-item">
        <span class="contact-icon"><svg viewBox="0 0 10 10"><path d="M5 0.5a3.2 3.2 0 0 0-3.2 3.2C1.8 6.2 5 9.5 5 9.5s3.2-3.3 3.2-5.8A3.2 3.2 0 0 0 5 0.5zm0 4.5a1.3 1.3 0 1 1 0-2.6 1.3 1.3 0 0 1 0 2.6z" fill="#fff"/></svg></span>
        <span>4816 Marlow Ct #306142<br>Houston, TX 77391</span>
      </li>
      <li class="contact-item">
        <span class="contact-icon"><svg viewBox="0 0 10 10"><path d="M2.2 0.8l1.6 2-0.9 1.2c0.6 1.3 1.6 2.3 2.9 2.9l1.2-0.9 2 1.6-1 1.6C4.4 9.2 0.8 5.6 0.6 1.8z" fill="#fff"/></svg></span>
        <span>713 555 0148</span>
      </li>
    </ul>

    <ul class="contact-list right">
      <li class="contact-item">
        <span class="contact-icon"><svg viewBox="0 0 10 10"><rect x="0.8" y="2" width="8.4" height="6" fill="none" stroke="#fff" stroke-width="1"/><path d="M0.8 2L5 5.5 9.2 2" fill="none" stroke="#fff" stroke-width="1"/></svg></span>
        <span>Gerald@thequillstoneframeworks.com</span>
      </li>
      <li class="contact-item">
        <span class="contact-icon"><svg viewBox="0 0 10 10"><circle cx="5" cy="5" r="4" fill="none" stroke="#fff" stroke-width="0.9"/><ellipse cx="5" cy="5" rx="1.8" ry="4" fill="none" stroke="#fff" stroke-width="0.8"/><path d="M1 5h8" stroke="#fff" stroke-width="0.8"/></svg></span>
        <span>www.thequillstoneframeworks.com</span>
      </li>
    </ul>
  </section>

</main>
</body>
</html>
```